Brivane - Business Cards for a new venture

create business card for a startup classified business dealing in construction materials, the cards need to have a professional look but modern, more serious than playful, one of the samples must include the official font (attached), please explore using the official colors in the company's logo

Target Market(s)

Energy sector

Contact Information for Business Card

Font styles to use
Other font styles liked:
• suissnord

Requirements
Must have
• corporate colors (in logo attached)
Nice to have
• Official font (in one of the samples) font is : suissnord
Should not have
• Cartoonish look

```html
<!DOCTYPE html>
<html lang="en">
<head>
<meta charset="utf-8">
<title>Brivane – Business Card</title>
<link rel="stylesheet" href="https://fonts.googleapis.com/css2?family=Exo+2:wght@400;500&display=swap">
<style>
  :root {
    --brand-blue: #31578a;
    --brand-grey: #9a9b9d;
    --bar-grey: #d1d2d4;
    --paper: #ffffff;
    --backdrop: #ebe8e3;
    --ink-light: #ffffff;
    --ink-soft: #e6ecf4;
  }
  * { box-sizing: border-box; margin: 0; padding: 0; }
  html, body { width: 1200px; height: 1200px; overflow: hidden; }
  body {
    background: var(--backdrop);
    font-family: "Exo 2", sans-serif;
    position: relative;
  }
  .card {
    position: absolute;
    left: 168px;
    width: 869px;
    height: 510px;
    overflow: hidden;
    box-shadow: 0 4px 14px rgba(0,0,0,0.12);
  }
  .card-front { top: 74px; background: var(--paper); }
  .card-back { top: 618px; background: var(--brand-blue); color: var(--ink-light); }

  .brand-name {
    position: absolute;
    left: 0; right: 0;
    top: 250px;
    text-align: center;
    font-size: 64px;
    font-weight: 500;
    letter-spacing: 10px;
    color: var(--brand-blue);
  }
  .front-bands { position: absolute; left: 0; top: 0; width: 869px; height: 510px; }

  .contact-strip {
    position: absolute;
    top: 448px;
    left: 0;
    display: flex;
    align-items: center;
    height: 36px;
  }
  .contact-item {
    position: absolute;
    display: flex;
    align-items: center;
    gap: 14px;
    font-size: 28px;
    color: var(--ink-light);
    white-space: nowrap;
  }
  .contact-item.email { left: 48px; }
  .contact-item.web { left: 392px; }
  .icon { width: 30px; height: 30px; flex: none; }

  .person-name {
    position: absolute;
    left: 41px; top: 36px;
    font-size: 38px;
    font-weight: 500;
  }
  .person-rule {
    position: absolute;
    left: 41px; top: 90px;
    width: 210px; height: 3px;
    background: linear-gradient(90deg, rgba(255,255,255,0.7), rgba(255,255,255,0));
  }
  .person-role {
    position: absolute;
    left: 41px; top: 98px;
    font-size: 23px;
    color: var(--ink-soft);
  }
  .detail {
    position: absolute;
    left: 41px;
    display: flex;
    align-items: flex-start;
    gap: 16px;
    font-size: 28px;
    line-height: 42px;
    color: var(--ink-soft);
  }
  .detail .icon { margin-top: 6px; }
  .detail.phone { top: 228px; }
  .detail.office { top: 286px; }
  .detail.home { top: 391px; }
</style>
</head>
<body>

<section class="card card-front" aria-label="Business card front">
  <div class="brand-name">BRIVANE</div>
  <svg class="front-bands" viewBox="0 0 869 510" aria-hidden="true">
    <rect x="0" y="390" width="610" height="39" fill="var(--bar-grey)"/>
    <path d="M0 429 H610 V418 H762 L792 468 L822 418 H869 V510 H0 Z" fill="var(--brand-blue)"/>
  </svg>
  <div class="contact-strip">
    <div class="contact-item email">
      <svg class="icon" viewBox="0 0 30 30" aria-hidden="true">
        <circle cx="15" cy="15" r="14" fill="#fff"/>
        <rect x="8" y="10" width="14" height="10" fill="none" stroke="var(--brand-blue)" stroke-width="1.6"/>
        <path d="M8 10 L15 16 L22 10" fill="none" stroke="var(--brand-blue)" stroke-width="1.6"/>
      </svg>
      <span>info@brivane.com</span>
    </div>
    <div class="contact-item web">
      <svg class="icon" viewBox="0 0 30 30" aria-hidden="true">
        <circle cx="15" cy="15" r="14" fill="#fff"/>
        <circle cx="15" cy="15" r="7" fill="none" stroke="var(--brand-blue)" stroke-width="1.5"/>
        <ellipse cx="15" cy="15" rx="3" ry="7" fill="none" stroke="var(--brand-blue)" stroke-width="1.2"/>
        <line x1="8" y1="15" x2="22" y2="15" stroke="var(--brand-blue)" stroke-width="1.2"/>
      </svg>
      <span>www.brivane.com</span>
    </div>
  </div>
</section>

<section class="card card-back" aria-label="Business card back">
  <h1 class="person-name">Rohan Desai</h1>
  <div class="person-rule"></div>
  <p class="person-role">Managing Director</p>

  <div class="detail phone">
    <svg class="icon" viewBox="0 0 30 30" aria-hidden="true">
      <circle cx="15" cy="15" r="14" fill="#fff"/>
      <path d="M10 8 L13 8 L14 12 L12 13.5 C13 16 14 17 16.5 18 L18 16 L22 17 L22 20 C22 21 21 22 20 22 C14 22 8 16 8 10 C8 9 9 8 10 8 Z" fill="var(--brand-blue)"/>
    </svg>
    <span>9876501234</span>
  </div>

  <div class="detail office">
    <svg class="icon" viewBox="0 0 30 30" aria-hidden="true">
      <circle cx="15" cy="15" r="14" fill="#fff"/>
      <path d="M15 23 C11 18 10 15.5 10 13 A5 5 0 0 1 20 13 C20 15.5 19 18 15 23 Z" fill="var(--brand-blue)"/>
      <circle cx="15" cy="13" r="2" fill="#fff"/>
    </svg>
    <span>Brivane, Near Orion Building,&nbsp; Kesar Road,<br>Ravipur, Gujarat, India.</span>
  </div>

  <div class="detail home">
    <svg class="icon" viewBox="0 0 30 30" aria-hidden="true">
      <circle cx="15" cy="15" r="14" fill="#fff"/>
      <path d="M8 15 L15 8.5 L22 15 L20 15 L20 21 L10 21 L10 15 Z" fill="var(--brand-blue)"/>
      <rect x="13.5" y="17" width="3" height="4" fill="#fff"/>
    </svg>
    <span>Opp. Lotus Tower, Near Central Trust Bank,<br>Kesar Road, Ravipur, Gujarat, India.</span>
  </div>
</section>

</body>
</html>
```